Erotik Online Shop
Immer wieder gerne. Eine tolle Kommunikation und ein tolles Ergebnis
Zielgruppe
Kunden des Online Shops, vorzugsweise schwule Männer wobei der Shop auch die hetero Ziegruppe bedienen bzw. befriedigen kann.
Aufgabenstellung
Für den Relounch unserers Online Shops benötigen wir mehrer Grafiken für die Startseite des Shops sowie eventuell einen Überabreitung unseres Logos.

```html
<!DOCTYPE html>
<html lang="de">
<head>
<meta charset="utf-8">
<title>Lustbox24 – Startseitengrafiken</title>
<link rel="stylesheet" href="https://fonts.googleapis.com/css2?family=Anton&family=Archivo+Black&family=Arvo:wght@700&family=Oswald:wght@500;700&display=swap">
<style>
:root{
  --bg:#ffffff;
  --dark:#262626;
  --dark-2:#3a3a3a;
  --mid:#8c8c8c;
  --light:#d6d6d6;
  --red:#d8262c;
  --red-dark:#a3161b;
  --white:#ffffff;
  --black:#111111;
}
*{margin:0;padding:0;box-sizing:border-box}
html,body{width:1200px;height:1200px;overflow:hidden;background:var(--bg)}
.canvas{position:relative;width:1200px;height:1200px;font-family:"Oswald",sans-serif}

/* hero banner */
.hero{position:absolute;left:108px;top:15px;width:972px;height:423px;border-radius:18px;overflow:hidden;
  background:repeating-linear-gradient(0deg,#2e2e2e 0 3px,#262626 3px 6px)}
.hero-photo{position:absolute;left:300px;top:0;width:672px;height:423px;
  background:radial-gradient(ellipse at 60% 45%,#d9d9d9 0%,#9a9a9a 35%,#4a4a4a 70%,#2a2a2a 100%)}
.hero-tag{position:absolute;left:42px;top:53px;width:338px;height:255px;border-radius:26px;
  background:linear-gradient(#ffffff,#e4e4e4);box-shadow:0 4px 12px rgba(0,0,0,.5);padding:18px 0 0 24px}
.hero-tag .line{font-family:"Archivo Black",sans-serif;font-size:33px;line-height:40px;letter-spacing:-.5px;color:var(--black)}
.hero-tag .line.red{color:var(--red)}
.hero-word{display:flex;align-items:center;font-family:"Arvo",serif;font-weight:700;font-size:118px;line-height:130px;color:#cfcfcf;margin-top:4px}
.go{display:inline-flex;align-items:center;justify-content:center;border-radius:50%;background:radial-gradient(circle at 40% 35%,#444,#000)}
.hero-word .go{width:92px;height:92px;margin:0 2px}
.hero-band{position:absolute;left:0;bottom:0;width:100%;height:88px;background:linear-gradient(rgba(120,120,120,.7),rgba(70,70,70,.85))}
.hero-slogan{position:absolute;left:30px;bottom:10px;font-family:"Oswald",sans-serif;font-weight:700;font-size:56px;line-height:70px;color:var(--white);letter-spacing:-.5px}
.hero-shop{position:absolute;right:40px;bottom:16px;display:flex;align-items:center;gap:8px;font-family:"Oswald",sans-serif;font-weight:500;font-size:52px;line-height:60px;color:#e8e8e8}
.hero-brand{position:absolute;right:42px;bottom:96px;font-family:"Oswald",sans-serif;font-weight:700;font-size:24px;color:var(--white)}

/* service bubble */
.service{position:absolute;left:0;top:0;width:1200px;height:1200px;pointer-events:none}
.service-title{position:absolute;left:145px;top:470px;font-family:"Anton",sans-serif;font-size:80px;line-height:96px;color:#b8b8b8;letter-spacing:1px}
.service-bang{position:absolute;left:650px;top:470px;font-family:"Anton",sans-serif;font-size:250px;line-height:250px;color:#b8b8b8}
.service-list{position:absolute;left:140px;top:568px;width:500px;list-style:none;text-align:center;font-family:"Oswald",sans-serif;font-weight:700;font-size:21px;line-height:38px;color:var(--white)}
.service-list .star{color:var(--red)}

/* small panels */
.panel{position:absolute;top:762px;height:423px;border-radius:14px;overflow:hidden;background:repeating-linear-gradient(0deg,#2c2c2c 0 3px,#242424 3px 6px);box-shadow:0 0 0 1px #bdbdbd}
.panel-head{height:78px;background:linear-gradient(#ffffff,#e6e6e6);text-align:center;padding-top:12px;font-family:"Oswald",sans-serif;font-weight:700;font-size:22px;line-height:26px;color:var(--black)}
.panel-head .red{color:var(--red)}
.pay{list-style:none;padding:14px 0 0 14px}
.pay li{display:flex;align-items:center;gap:14px;height:56px;font-family:"Oswald",sans-serif;font-weight:700;font-size:17px;line-height:19px;color:var(--white)}
.pay .chip{flex:none;width:46px;height:32px;border-radius:4px;background:linear-gradient(#f2f2f2,#bcbcbc)}
.panel-foot{position:absolute;left:0;bottom:0;width:100%;height:44px;background:linear-gradient(#fafafa,#dcdcdc);display:flex;align-items:center;justify-content:space-between;padding:0 8px 0 12px;font-family:"Oswald",sans-serif;font-weight:700;font-size:16px;color:var(--black)}
.panel-foot .go{width:34px;height:34px}
.steps{list-style:none;padding:14px 0 0 8px}
.steps li{display:flex;align-items:center;gap:6px;height:92px}
.steps .big{display:block;font-family:"Anton",sans-serif;font-size:46px;line-height:46px;color:var(--white)}
.steps .small{display:block;font-family:"Oswald",sans-serif;font-weight:700;font-size:18px;line-height:20px;color:var(--white)}
.promo-photo{position:absolute;inset:0;background:radial-gradient(ellipse at 70% 45%,#b5b5b5 0%,#6e6e6e 45%,#333 100%)}
.promo-free{position:absolute;left:40px;top:10px;width:60px;height:250px;display:flex;align-items:center;justify-content:center}
.promo-free span{transform:rotate(90deg);font-family:"Anton",sans-serif;font-size:86px;line-height:86px;color:var(--white);white-space:nowrap}
.promo-price{position:absolute;left:112px;top:95px;width:82px;height:82px;border-radius:50%;background:var(--white);border:4px dashed var(--red);display:flex;align-items:center;justify-content:center;font-family:"Anton",sans-serif;font-size:38px;color:var(--red)}
.promo-box{position:absolute;left:10px;bottom:12px;width:205px;height:140px;border-radius:14px;background:linear-gradient(#ffffff,#e2e2e2);text-align:center;padding-top:8px}
.promo-box .l1{font-family:"Oswald",sans-serif;font-weight:700;font-size:26px;line-height:28px;color:var(--black)}
.promo-box .l2{font-family:"Oswald",sans-serif;font-weight:700;font-size:24px;line-height:26px;color:var(--red)}
.promo-now{display:flex;align-items:center;justify-content:center;font-family:"Arvo",serif;font-weight:700;font-size:64px;line-height:70px;color:#c9c9c9}
.promo-now .go{width:52px;height:52px;margin:0 2px}
</style>
</head>
<body>
<main class="canvas">

  <section class="hero">
    <div class="hero-photo" role="img" aria-label="Schwarzweißfoto eines Männeroberkörpers, der den Bund seiner weißen Unterhose herunterzieht"></div>
    <div class="hero-tag">
      <p class="line">LOVE YOUR MAN!</p>
      <p class="line red">LOVE YOURSELF!</p>
      <p class="hero-word">T<span class="go" aria-hidden="true"><svg width="44" height="52" viewBox="0 0 44 52"><path d="M8 4 L38 26 L8 48 L8 34 L20 26 L8 18 Z" fill="#e6393f"/></svg></span>YS</p>
    </div>
    <p class="hero-brand">lustbox24.de</p>
    <div class="hero-band"></div>
    <p class="hero-slogan">Alles was Mann braucht</p>
    <p class="hero-shop">
      <svg width="54" height="44" viewBox="0 0 54 44" aria-hidden="true"><path d="M2 4 H12 L18 30 H46 L52 10 H15" fill="none" stroke="#e8e8e8" stroke-width="4" stroke-linejoin="round"/><circle cx="22" cy="38" r="4" fill="#e8e8e8"/><circle cx="42" cy="38" r="4" fill="#e8e8e8"/></svg>
      shop
    </p>
  </section>

  <svg class="service" viewBox="0 0 1200 1200" aria-hidden="true">
    <defs>
      <linearGradient id="bubbleFill" x1="0" y1="0" x2="0" y2="1">
        <stop offset="0" stop-color="#333"/><stop offset="1" stop-color="#1f1f1f"/>
      </linearGradient>
    </defs>
    <path d="M128 452 H738 Q756 452 756 470 V730 Q756 748 738 748 H205 L130 860 L132 748 H128 Q110 748 110 730 V470 Q110 452 128 452 Z"
          fill="url(#bubbleFill)" stroke="#d8262c" stroke-width="11" stroke-linejoin="round"/>
  </svg>
  <h2 class="service-title">UNSER SERVICE</h2>
  <div class="service-bang" aria-hidden="true">!</div>
  <ul class="service-list">
    <li><span class="star">*</span>Geld zurück Grantie<span class="star">*</span> Diskrete Verpackung<span class="star">*</span></li>
    <li><span class="star">*</span>Kein Mindestbestellwert<span class="star">*</span></li>
    <li><span class="star">*</span>Faire &amp; günstige Versandkosten<span class="star">*</span></li>
    <li><span class="star">*</span>Online Shopping seit 1999<span class="star">*</span></li>
  </ul>

  <section class="panel panel-payment" style="left:386px;width:222px">
    <h3 class="panel-head">WIR<br><span class="red">AKZEPTIEREN</span></h3>
    <ul class="pay">
      <li><span class="chip"></span>Kartenpay</li>
      <li><span class="chip"></span>Globalkarte</li>
      <li><span class="chip"></span>Netzbörse</li>
      <li><span class="chip"></span>Direkt-<br>überweisung</li>
      <li><span class="chip"></span>Vorkasse</li>
    </ul>
    <div class="panel-foot">Mehr Information<span class="go"><svg width="16" height="18" viewBox="0 0 44 52"><path d="M8 4 L38 26 L8 48 L8 34 L20 26 L8 18 Z" fill="#e6393f"/></svg></span></div>
  </section>

  <section class="panel panel-partner" style="left:620px;width:225px">
    <h3 class="panel-head">PARTNER<br><span class="red">PROGRAMM</span></h3>
    <ul class="steps">
      <li><svg width="54" height="48" viewBox="0 0 54 48" aria-hidden="true"><path d="M4 26 L18 42 L50 6" fill="none" stroke="#d8262c" stroke-width="10" stroke-linecap="round" stroke-linejoin="round"/></svg><span><span class="big">JETZT</span><span class="small">REGISTRIEREN</span></span></li>
      <li><svg width="54" height="48" viewBox="0 0 54 48" aria-hidden="true"><path d="M4 26 L18 42 L50 6" fill="none" stroke="#d8262c" stroke-width="10" stroke-linecap="round" stroke-linejoin="round"/></svg><span><span class="big">BANNER</span><span class="small">PLATZIEREN</span></span></li>
      <li><svg width="54" height="48" viewBox="0 0 54 48" aria-hidden="true"><path d="M4 26 L18 42 L50 6" fill="none" stroke="#d8262c" stroke-width="10" stroke-linecap="round" stroke-linejoin="round"/></svg><span><span class="big">GELD</span><span class="small">VERDIENEN</span></span></li>
    </ul>
    <div class="panel-foot">Mehr Information<span class="go"><svg width="16" height="18" viewBox="0 0 44 52"><path d="M8 4 L38 26 L8 48 L8 34 L20 26 L8 18 Z" fill="#e6393f"/></svg></span></div>
  </section>

  <section class="panel panel-newsletter" style="left:855px;width:225px">
    <div class="promo-photo" role="img" aria-label="Schwarzweißfoto eines nackten Männeroberkörpers"></div>
    <div class="promo-free"><span>FREE</span></div>
    <div class="promo-price">0,-€</div>
    <div class="promo-box">
      <p class="l1">NEWSLETTER</p>
      <p class="l2">REGISTRIEREN</p>
      <p class="promo-now">N<span class="go"><svg width="26" height="30" viewBox="0 0 44 52"><path d="M8 4 L38 26 L8 48 L8 34 L20 26 L8 18 Z" fill="#e6393f"/></svg></span>W</p>
    </div>
  </section>

</main>
</body>
</html>
```